Business Card design for Recruiter providing Recruitment Staff Augmentation services

I need a double sided business card. I have used Zek to print cards in the past and really like their quality. I have a logo but need to change the tagline that is part of the graphic.

The tagline currently reads and Connnecting people with careers - but it should be removed.

The back should look like a notecard for writing a to do list with the first to-do Augment Recruiting Staff

```html
<!DOCTYPE html>
<html lang="en">
<head>
<meta charset="utf-8">
<title>Talent Summit — Business Card</title>
<link rel="stylesheet" href="https://fonts.googleapis.com/css2?family=Montserrat:wght@400;500;600&display=swap">
<style>
  :root {
    --backdrop: #57493d;
    --paper: #ffffff;
    --navy: #0a4261;
    --rust: #c6391e;
    --note-paper: #e4dcdb;
    --rule: #9a9595;
    --note-ink: #5c5656;
    --light-ink: #ffffff;
  }
  * { margin: 0; padding: 0; box-sizing: border-box; }
  html, body {
    width: 1200px;
    height: 987px;
    overflow: hidden;
    background: var(--backdrop);
    font-family: "Montserrat", Arial, sans-serif;
  }
  .card {
    position: absolute;
    left: 293px;
    width: 615px;
    height: 352px;
    overflow: hidden;
    box-shadow: 0 2px 4px rgba(0,0,0,0.35);
  }
  .card-front { top: 130px; background: var(--paper); }
  .card-back { top: 505px; background: var(--note-paper); }
  .card-art { position: absolute; inset: 0; width: 100%; height: 100%; }

  .brand {
    position: absolute;
    left: 42px;
    top: 42px;
    display: flex;
    align-items: center;
    gap: 10px;
  }
  .brand-dot {
    width: 30px;
    height: 30px;
    border-radius: 50%;
    background: var(--rust);
  }
  .brand-name {
    font-size: 31px;
    font-weight: 500;
    color: var(--navy);
    letter-spacing: 0.5px;
    line-height: 1;
  }
  .person { position: absolute; left: 42px; top: 116px; }
  .person-name {
    font-size: 22px;
    font-weight: 600;
    color: var(--navy);
    letter-spacing: 0.8px;
    line-height: 1.1;
  }
  .person-role {
    font-size: 17px;
    font-weight: 400;
    color: var(--rust);
    letter-spacing: 0.4px;
    line-height: 1.2;
  }
  .contact-list {
    position: absolute;
    right: 22px;
    top: 180px;
    list-style: none;
    color: var(--light-ink);
    font-size: 15.5px;
    letter-spacing: 0.4px;
  }
  .contact-item {
    display: flex;
    justify-content: flex-end;
    align-items: center;
    gap: 8px;
    height: 23.5px;
  }
  .contact-icon { width: 14px; height: 14px; fill: var(--light-ink); flex: none; }
  .address {
    position: absolute;
    right: 22px;
    top: 303px;
    color: var(--light-ink);
    font-size: 15.5px;
    letter-spacing: 0.4px;
  }
  .note-site {
    position: absolute;
    left: 410px;
    top: 286px;
    font-size: 15.5px;
    color: var(--note-ink);
  }
</style>
</head>
<body>

<section class="card card-front" aria-label="Card front">
  <svg class="card-art" viewBox="0 0 525 300" preserveAspectRatio="none" aria-hidden="true">
    <path fill="var(--rust)" d="M132,300 C150,200 215,155 325,115 C440,75 498,45 510,12 L525,0 L525,300 Z"/>
    <path fill="var(--navy)" stroke="#ffffff" stroke-width="1.6"
          d="M138,301 C160,215 225,175 335,135 C445,95 495,60 511,-1 L526,-1 L526,301 Z"/>
  </svg>

  <div class="brand">
    <span class="brand-dot"></span>
    <span class="brand-name">TALENT SUMMIT</span>
  </div>

  <div class="person">
    <p class="person-name">DANIEL REYES</p>
    <p class="person-role">CEO/FOUNDER</p>
  </div>

  <ul class="contact-list">
    <li class="contact-item">555 201 4410
      <svg class="contact-icon" viewBox="0 0 16 16"><path d="M3.5 1l2.5 3-1.5 1.8c.9 2 2.5 3.6 4.6 4.6L10.9 9l3 2.5-1.4 2.8C7 14 2 9 1.7 3.5z"/></svg>
    </li>
    <li class="contact-item">555 318 7725
      <svg class="contact-icon" viewBox="0 0 16 16"><path d="M4.5 0h7a1 1 0 0 1 1 1v14a1 1 0 0 1-1 1h-7a1 1 0 0 1-1-1V1a1 1 0 0 1 1-1zm.6 2v10.5h5.8V2z"/></svg>
    </li>
    <li class="contact-item">555 462 0938
      <svg class="contact-icon" viewBox="0 0 16 16"><path d="M4 1h8v4H4zM1 6h14v6h-2.5v-2h-9v2H1zm3.5 5h7v4h-7z"/></svg>
    </li>
    <li class="contact-item">hello@talentsummit.co
      <svg class="contact-icon" viewBox="0 0 16 16"><path d="M1 3h14v1.2L8 9 1 4.2zm0 2.6l7 4.8 7-4.8V13H1z"/></svg>
    </li>
    <li class="contact-item">www.talentsummit.co
      <svg class="contact-icon" viewBox="0 0 16 16"><circle cx="8" cy="8" r="7"/><path fill="var(--navy)" d="M5 4.5c1.5-.6 3 0 3.4 1.3-.9.6-2 .4-2.4 1.5-.4 1 .7 1.8 0 2.8C5 9.6 4 8.2 4.3 6.5zm5 3.5c1 .2 2 1 1.8 2.3-.4.9-1.4 1.6-2.2 1.4.2-1.2-.6-2.5.4-3.7z"/></svg>
    </li>
  </ul>

  <p class="address">2140 Cedar Ridge Road, Juneau, Alaska 99801</p>
</section>

<section class="card card-back" aria-label="Card back, note lines">
  <svg class="card-art" viewBox="0 0 525 300" preserveAspectRatio="none" aria-hidden="true">
    <g stroke="var(--rule)" stroke-width="0.8">
      <line x1="62" y1="53" x2="482" y2="53"/>
      <line x1="34" y1="93" x2="482" y2="93"/>
      <line x1="34" y1="133" x2="482" y2="133"/>
      <line x1="34" y1="173" x2="482" y2="173"/>
      <line x1="34" y1="213" x2="482" y2="213"/>
      <line x1="34" y1="253" x2="344" y2="253"/>
    </g>
  </svg>
  <p class="note-site">www.talentsummit.co</p>
</section>

</body>
</html>
```